Northfield Sum Tutor

Need a new design for northfieldsumtutor.com as we are having a new backend developed. The design should be fun, and visually interesting for kids, yet sophisticated enough for parents, teachers and school districts.

Our main competitor is qvo.com and we like their concept. The colors should pop, and be exciting. The layout should be simple. Because we are having our website developed, we only will need the design and no functionality, a Photoshop or Fireworks file will work best.

We like the simplicity of our existing site, but it looks fairly unexciting. Here is a version our developers gave us. We do not like the design.

http://velunteworks.com/velunteframe/northfieldsumtutor/layout/

The winning designer will most likely get more work from us as we make modifications.
Updates

Target Market(s)

Parents, Teachers, students

Industry/Entity Type

School

Requirements
Must have
• login at the top
social icons for recommend and like
Showcase area for features and testimonials

```html
<!DOCTYPE html>
<html lang="en">
<head>
<meta charset="utf-8">
<title>Northfield Sum Tutor</title>
<link rel="stylesheet" href="https://fonts.googleapis.com/css2?family=Marcellus&family=Open+Sans:wght@400;600;700&family=Arimo:wght@400;700&family=Permanent+Marker&display=swap">
<style>
:root{
  --nav:#2c2f34;
  --nav-line:#3b3f45;
  --hero:#3f4349;
  --hero-deep:#34373c;
  --white:#ffffff;
  --ink:#333333;
  --muted:#555555;
  --blue:#1b9ad8;
  --blue-dark:#0f74b3;
  --orange:#f5a300;
  --orange-dark:#d88400;
  --green:#6cb01a;
  --green-dark:#4d8b0c;
  --red:#d3202b;
  --red-dark:#a8141d;
  --board:#3a3c3f;
  --panel:#f4f4f4;
  --border:#d8d8d8;
  --foot:#eeeeef;
  --foot-low:#e4e4e5;
  --gold:#e9a000;
}
*{box-sizing:border-box;margin:0;padding:0}
html,body{width:961px;height:1200px;overflow:hidden}
body{font-family:"Arimo",Arial,sans-serif;color:var(--ink);background:var(--white);position:relative}
a{color:inherit;text-decoration:none}

.topbar{position:absolute;left:0;top:0;width:961px;height:47px;background:var(--nav);border-bottom:1px solid #222}
.brand{position:absolute;left:85px;top:9px;font-family:"Marcellus",serif;font-size:25px;color:var(--white);display:flex;align-items:center;gap:10px}
.brand-mark{width:22px;height:18px;background:var(--white)}
.main-nav{position:absolute;left:411px;top:0;height:47px;display:flex}
.main-nav a{display:flex;align-items:center;padding:0 16px;height:47px;font-size:12px;color:#c9cbcf;border-left:1px solid var(--nav-line)}
.main-nav a.current{color:var(--white);font-weight:700}
.main-nav a.login{background:#1f2125;color:var(--white);padding:0 17px;border-right:1px solid var(--nav-line)}
.login-menu{position:absolute;left:782px;top:47px;width:96px;background:#1f2125;z-index:3;padding:2px 0}
.login-menu a{display:flex;align-items:center;gap:7px;height:21px;padding-left:8px;font-size:9.5px;color:#e6e6e6;border-bottom:1px solid #2e3035}
.login-menu a:last-child{border-bottom:0}
.login-menu i{width:6px;height:6px;background:#e6e6e6;border-radius:50%;display:block}

.hero{position:absolute;left:0;top:48px;width:961px;height:203px;background:linear-gradient(#44484e,var(--hero-deep))}
.hero-art{position:absolute;left:86px;top:0;width:392px;height:203px;background:linear-gradient(90deg,#2a2c30 0%,#4d7aa8 45%,#8aa7c4 70%,#3f4349 100%);border-radius:0}
.hero-copy{position:absolute;left:488px;top:50px;width:380px;color:var(--white)}
.hero-copy h1{font-family:"Open Sans",sans-serif;font-weight:400;font-size:29px;margin-bottom:6px}
.hero-copy p{font-size:14.5px;line-height:17px;color:#eeeeee}
.btn{display:inline-flex;align-items:center;justify-content:center;color:var(--white);font-family:"Open Sans",sans-serif;font-weight:600;border-radius:14px}
.btn-blue{background:linear-gradient(#2fb1ee,var(--blue-dark));box-shadow:inset 0 1px 0 rgba(255,255,255,.35)}
.hero .btn{margin-top:15px;width:116px;height:28px;font-size:11.5px}
.slider-dots{position:absolute;left:825px;top:176px;display:flex;gap:6px}
.slider-dots span{width:10px;height:10px;border-radius:50%;background:#26282c}
.slider-dots span.on{background:#d8d8d8}

.content{position:absolute;left:82px;top:251px;width:604px}
.section-title{font-family:"Open Sans",sans-serif;color:var(--blue);font-weight:600;font-size:19px}
.edu-title{position:absolute;top:23px;left:0}
.cards{position:absolute;top:61px;left:0;display:flex;gap:4px}
.card{width:148px;height:217px;background:linear-gradient(#ffffff,#ececec);border:1px solid #cfcfcf;border-top:0;clip-path:polygon(0 0,100% 0,100% 92%,92% 100%,8% 100%,0 92%);position:relative}
.board{height:107px;background:var(--nav);padding:6px}
.board-inner{height:95px;border:2px solid #c8c8c8;background:var(--board);display:flex;align-items:center;justify-content:center;text-align:center;font-family:"Permanent Marker",cursive;color:var(--white);font-size:16.5px;line-height:28px;letter-spacing:.5px;position:relative}
.board-inner::after{content:"";position:absolute;left:19px;bottom:3px;width:22px;height:3px;background:#e6e6e6}
.card p{font-size:9.6px;line-height:11.2px;padding:6px 6px 0 6px;color:#222;height:77px}
.card-action{position:absolute;left:35px;top:186px;display:flex;align-items:center;gap:5px}
.btn-orange{background:linear-gradient(#ffc030,var(--orange-dark));font-size:9.5px;font-weight:600;height:21px;width:62px}
.plus{width:16px;height:16px;border-radius:50%;display:flex;align-items:center;justify-content:center;color:var(--white);font-weight:700;font-size:12px;line-height:1}
.plus-orange{background:var(--orange)}
.plus-blue{background:var(--blue-dark)}

.rule{position:absolute;left:0;width:604px;height:6px;background:repeating-linear-gradient(135deg,#d6d6d6 0 1px,transparent 1px 3px)}
.rule-action{position:absolute;display:flex;align-items:center;gap:8px;background:var(--white);padding:0 6px}
.rule-action .btn{height:24px;font-size:10.5px;font-weight:400}

.program{position:absolute;top:355px;left:0;display:flex;align-items:center;gap:9px}
.program-icon{width:36px;height:32px;background:linear-gradient(#2f6f3f,#b8872c)}
.program .section-title{font-size:19px}
.photos{position:absolute;top:394px;left:0;display:flex;gap:64px}
.photo{width:134px;height:108px;border-radius:6px;border:1px solid #ddd}
.photo-1{background:linear-gradient(135deg,#d8c7b6,#8a5a3e 55%,#ece4dc)}
.photo-2{background:linear-gradient(135deg,#f5a59a,#a0543a 55%,#5d4a40)}
.photo-3{background:linear-gradient(135deg,#9fb7a6,#506a5a 55%,#3a3f52)}
.about{position:absolute;top:533px;left:0;width:590px}
.about h2{font-family:"Open Sans",sans-serif;font-size:19px;font-weight:600;color:#222;margin-bottom:10px}
.about p{font-family:"Open Sans",sans-serif;font-size:13.6px;line-height:18px;color:var(--muted);margin-bottom:15px}
.about strong{color:var(--blue);font-weight:700}

.sidebar{position:absolute;left:693px;top:267px;width:180px}
.widget{border:1px solid var(--border);background:var(--white);margin-bottom:7px}
.widget-body{padding:8px 13px 6px 13px}
.widget h3{font-family:"Open Sans",sans-serif;font-weight:600;font-size:15px;line-height:17px;color:var(--blue);margin-bottom:5px}
.widget p{font-size:8px;line-height:10px;color:#555}
.widget-foot{background:var(--panel);border-top:1px solid var(--border);display:flex;align-items:center;justify-content:center}
.widget-foot .btn{width:152px;height:23px;font-size:10.5px;font-weight:400}
.field{display:flex;align-items:center;margin-top:6px;font-size:8px;font-weight:700}
.field span{width:33px}
.field i{flex:1;height:12px;border:1px solid #ccc;background:#fafafa}
.signup .widget-foot{height:44px}
.voucher h3{color:var(--green-dark)}
.voucher .widget-foot{height:45px}
.btn-green{background:linear-gradient(#86cc22,var(--green-dark))}
.btn-red{background:linear-gradient(#ee3d46,var(--red-dark))}
.btn-gold{background:linear-gradient(#ffc030,var(--orange-dark))}
.seal{width:96px;height:96px;margin:8px auto 6px;border-radius:50%;background:radial-gradient(circle at 45% 40%,#d6323a,#98141b);display:flex;align-items:center;justify-content:center;text-align:center;color:var(--white);font-family:"Open Sans",sans-serif;font-weight:700;font-size:8.5px;line-height:13px}
.seal b{font-size:10px}
.guarantee .widget-body{padding:1px 13px 8px}
.guarantee .widget-foot{height:42px}
.quotes h3{color:var(--gold)}
.quotes .widget-foot{height:44px}

.footer{position:absolute;left:0;top:988px;width:961px;height:128px;background:var(--foot);border-top:1px solid #e0e0e0}
.quicklinks{position:absolute;left:96px;top:27px}
.footer h4{font-size:10.5px;font-weight:700;color:#333;margin-bottom:6px}
.quicklinks a{display:block;font-size:8.6px;line-height:14.3px;text-decoration:underline;color:#444}
.follow{position:absolute;left:593px;top:27px}
.social{display:flex;gap:7px;margin-top:21px}
.social span{width:26px;height:26px;border-radius:4px}
.bottom{position:absolute;left:0;top:1116px;width:961px;height:84px;background:var(--foot-low)}
.bottom-nav{position:absolute;left:96px;top:14px;display:flex;gap:23px;font-size:9.6px}
.bottom-nav a{text-decoration:underline;color:#444}
.bottom-nav a.current{color:var(--blue)}
.share{position:absolute;left:721px;top:14px;display:flex;gap:8px;font-size:9px}
.share span{height:15px;display:flex;align-items:center;padding:0 6px;border:1px solid #c4c4c4;background:#f7f7f7;border-radius:2px;color:#3a5a8c;font-weight:700}
.share span.count{color:#333;font-weight:400;background:var(--white)}
.copyright{position:absolute;left:93px;top:62px;font-size:9px;color:#444}
.copyright a{text-decoration:underline}
</style>
</head>
<body>

<header class="topbar">
  <div class="brand"><span class="brand-mark"></span>Northfield Sum Tutor</div>
  <nav class="main-nav">
    <a class="current" href="#">Home</a>
    <a href="#">About NST</a>
    <a href="#">Pricing</a>
    <a href="#">Learning Centers</a>
    <a href="#">Contact</a>
    <a class="login" href="#">Login</a>
  </nav>
</header>
<nav class="login-menu">
  <a href="#"><i></i>Parents Login</a>
  <a href="#"><i></i>Teachers Login</a>
  <a href="#"><i></i>Schools Login</a>
</nav>

<section class="hero">
  <div class="hero-art" role="img" aria-label="Cartoon student at a computer beside a step-by-step video instruction badge"></div>
  <div class="hero-copy">
    <h1>Video Tutorials</h1>
    <p>No Nonsense Video Instruction, students aren't distracted by ads, fancy graphics, or unnecessary animation. Just straight to the pont instruction.</p>
    <a class="btn btn-blue" href="#">Watch a Tutorial</a>
  </div>
  <div class="slider-dots"><span class="on"></span><span></span><span></span></div>
</section>

<main class="content">
  <h2 class="section-title edu-title">NST Online Math Education</h2>
  <div class="cards">
    <article class="card">
      <div class="board"><div class="board-inner">LEARNING<br>CENTERS</div></div>
      <p>These are the hubs for each course. Access the complete library of video tutorials, printed exercises, quizzes, and final exams.</p>
      <div class="card-action"><a class="btn btn-orange" href="#">GO NOW</a><span class="plus plus-orange">+</span></div>
    </article>
    <article class="card">
      <div class="board"><div class="board-inner">EVALUATION<br>CENTER</div></div>
      <p>Pre-tests, quizzes, and final exams are available to take online for each NST Course. These are also available in each learning center.</p>
      <div class="card-action"><a class="btn btn-orange" href="#">GO NOW</a><span class="plus plus-orange">+</span></div>
    </article>
    <article class="card">
      <div class="board"><div class="board-inner">PRINTED<br>EXERCISES</div></div>
      <p>These are the hubs for each course. Access the complete library of video tutorials, printed exercises, quizzes, and final exams.</p>
      <div class="card-action"><a class="btn btn-orange" href="#">GO NOW</a><span class="plus plus-orange">+</span></div>
    </article>
    <article class="card">
      <div class="board"><div class="board-inner">RESOURCE<br>CENTER</div></div>
      <p>Information, glossaries, and math skill games are available in the NST resource center. New content is uploaded as it becomes available.</p>
      <div class="card-action"><a class="btn btn-orange" href="#">GO NOW</a><span class="plus plus-orange">+</span></div>
    </article>
  </div>

  <div class="rule" style="top:303px"></div>
  <div class="rule-action" style="left:228px;top:294px"><a class="btn btn-blue" href="#" style="width:120px">Load More Articles</a><span class="plus plus-blue">+</span></div>
  <div class="rule" style="top:332px"></div>

  <div class="program">
    <div class="program-icon" role="img" aria-label="Stack of books with a graduation cap"></div>
    <h2 class="section-title">The Perfect Online Math Learning Program</h2>
  </div>
  <div class="photos">
    <div class="photo photo-1" role="img" aria-label="Parent helping a student at a laptop"></div>
    <div class="photo photo-2" role="img" aria-label="Two children learning together on a computer"></div>
    <div class="photo photo-3" role="img" aria-label="Teacher presenting to a classroom"></div>
  </div>

  <div class="about">
    <h2>Video, Printed Exercises, Quizzes and Exams</h2>
    <p>The <strong>perfect system to help students</strong> learn math and algebra. It's like having a personal tutor available every day!</p>
    <p>This powerful system is great for students who need extra help, students who are home schooled, or students looking to <strong>excel in math and Algebra.</strong></p>
  </div>

  <div class="rule" style="top:686px"></div>
  <div class="rule-action" style="left:251px;top:677px"><a class="btn btn-blue" href="#" style="width:80px">Learn More</a><span class="plus plus-blue">+</span></div>
</main>

<aside class="sidebar">
  <section class="widget signup">
    <div class="widget-body">
      <h3>Get 5 Lessons FREE!</h3>
      <p>Give us your name and email address and we'll send you a link to 5 video tutorials and 5 exercise worksheets, <b style="color:#222">absolutely FREE!</b></p>
      <div class="field"><span>Name*</span><i></i></div>
      <div class="field" style="margin-bottom:10px"><span>Email*</span><i></i></div>
    </div>
    <div class="widget-foot"><a class="btn btn-blue" href="#">YES, Send me 5 Lessons</a></div>
  </section>
  <section class="widget voucher">
    <div class="widget-body">
      <h3>Got a Dealnest Voucher ?</h3>
      <p>If you purchased special pricing at Dealnest, click the button below to register.</p>
    </div>
    <div class="widget-foot"><a class="btn btn-green" href="#">Dealnest</a></div>
  </section>
  <section class="widget guarantee">
    <div class="widget-body">
      <div class="seal"><span><b>30 DAYS</b><br>MONEY BACK<br>GUARANTEE</span></div>
      <p>Take a FULL 30 DAYS to evaluate Northfield Sum Tutor. If for any reason, you are not completely satisfied with this exceptional program, we will give you a complete refund, <b style="color:#222">GUARANTEED!</b></p>
    </div>
    <div class="widget-foot"><a class="btn btn-red" href="#">Join Now</a></div>
  </section>
  <section class="widget quotes">
    <div class="widget-body">
      <h3>What People are Saying</h3>
      <p>A good, systematic way to build your child's math skills over the summer, or even during the school year.<br><b style="color:#222">R. Calloway</b></p>
    </div>
    <div class="widget-foot"><a class="btn btn-gold" href="#">Read All</a></div>
  </section>
</aside>

<footer class="footer">
  <div class="quicklinks">
    <h4>NST Quicklinks</h4>
    <a href="#">Try NST for TODAY!</a>
    <a href="#">Contact NST</a>
    <a href="#">Login to your account</a>
    <a href="#">Terms of Service</a>
    <a href="#">Privacy Policy</a>
  </div>
  <div class="follow">
    <h4>Follow NST :</h4>
    <div class="social">
      <span style="background:#4fc3e8"></span>
      <span style="background:#3b5998"></span>
      <span style="background:#333"></span>
      <span style="background:#3d6ea8"></span>
      <span style="background:#3f78c0"></span>
      <span style="background:#555"></span>
      <span style="background:#3568c4"></span>
      <span style="background:#3c9a3c"></span>
      <span style="background:#e2e2e2;border:1px solid #ccc"></span>
    </div>
  </div>
</footer>
<div class="bottom">
  <nav class="bottom-nav">
    <a class="current" href="#">Home</a>
    <a href="#">About NST</a>
    <a href="#">Pricing</a>
    <a href="#">Learning Centers</a>
    <a href="#">Contact</a>
    <a href="#">Login</a>
  </nav>
  <div class="share">
    <span>Post</span><span class="count">7</span>
    <span>Like</span><span class="count">3</span>
  </div>
  <div class="copyright">© <a href="#">NorthfieldSumTutor.com</a></div>
</div>

</body>
</html>
```